Bramwell Dental personal information forms

We are a Dental Practice that require an update to our information forms, there are 3 versions of it.
I will attach our old ones, we need to keep the same information on there, we just want them to look better and use our current logo and colours.
Our website is www.bramwelldental-example.net
Our facebook is www.facebook.com/bramwelldentalkestonwalk/
..................................................................................................

Target Market(s)

Everyone, easy to read

Industry/Entity Type

Dental Clinic

Colors
0692cd
34a6d7
cee9f5
ffffff
0255a3
3276b5

Requirements
Must have
• Logo
• Our colours
• same information as the uploaded versions
Should not have
• any other colour besides the blues, black and white

```html
<!DOCTYPE html>
<html lang="en">
<head>
<meta charset="utf-8">
<title>Bramwell Dental – New Patient Form pg. 1</title>
<link href="https://fonts.googleapis.com/css2?family=Mulish:ital,wght@0,400;0,500;0,700;0,800;1,400;1,700&display=swap" rel="stylesheet">
<style>
  :root{
    --brand:#0692cd;
    --brand-bar:#0b87c6;
    --brand-soft:#cee9f5;
    --brand-mid:#34a6d7;
    --brand-deep:#0255a3;
    --brand-alt:#3276b5;
    --ink:#1a1a1a;
    --rule:#4a4a4a;
    --paper:#ffffff;
  }
  *{box-sizing:border-box;margin:0;padding:0}
  html,body{width:729px;height:1200px;overflow:hidden;background:var(--paper)}
  body{font-family:"Mulish",Arial,sans-serif;color:var(--ink)}
  .sheet{position:relative;width:729px;height:1200px;overflow:hidden;
    background:linear-gradient(to bottom,#ffffff 0%,#ffffff 72%,#e3f0f8 100%)}
  .masthead{position:absolute;left:0;top:0;width:729px;height:160px;
    background:linear-gradient(to bottom,var(--brand-soft) 0%,#e8f4fa 60%,#ffffff 100%)}
  .brand{position:absolute;right:22px;top:44px;display:flex;align-items:center;gap:10px;
    color:var(--brand);font-weight:500;font-size:44px;line-height:1}
  .brand-dot{width:14px;height:14px;border-radius:50%;background:var(--brand)}
  .practitioners{position:absolute;left:22px;top:180px;color:var(--brand-alt);font-style:italic;font-size:19.5px;line-height:26px}
  .form-tag{position:absolute;right:22px;top:211px;color:var(--brand);font-size:11px;letter-spacing:.3px}
  .form-tag b{font-size:15px;font-weight:800;margin-left:3px}
  .welcome{position:absolute;left:22px;top:255px;color:var(--brand);font-size:17px;font-weight:500}
  .intro{position:absolute;left:22px;top:284px;width:685px;font-size:12.3px;line-height:17.5px;text-align:justify;hyphens:auto}
  .intro em{font-weight:700}
  .form{position:absolute;left:22px;top:349px;width:685px}
  .band{height:22.7px;background:var(--brand-bar);color:#fff;font-weight:700;font-size:13px;letter-spacing:.3px;
    display:flex;align-items:center;justify-content:center}
  .row{position:relative;height:22.7px;border-bottom:1px solid var(--rule);font-size:12.3px}
  .row.tall{height:25.5px}
  .row.note{height:37px;font-style:italic;font-size:12.2px;line-height:16px}
  .row.note span{position:absolute;left:4px;top:2px;right:4px}
  .f{position:absolute;bottom:3px;left:4px;white-space:nowrap}
  .c-third{left:233px}.c-mid{left:347px}.c-far{left:460px}
  .t2{left:176px}.t3{left:347px}.t4{left:518px}
  .g2{left:141px}.g3{left:279px}.g4{left:415px}.g5{left:554px}
  .slash1{left:543px}.slash2{left:623px}
  .yn{position:absolute;right:6px;bottom:3px;font-weight:800}
  .box{display:inline-block;width:8px;height:8px;border:1px solid var(--ink);margin:0 4px 0 2px;vertical-align:0}
  .gap-7{height:7px}.gap-5{height:5px}
</style>
</head>
<body>
<div class="sheet">
  <div class="masthead" role="img" aria-label="Soft blue decorative header wave"></div>

  <div class="brand"><span class="brand-dot"></span><span>Bramwell Dental</span></div>

  <div class="practitioners">Dr. Peter Kallinos &amp; Dr. Hugh Barrett<br>Dental Surgeons</div>
  <div class="form-tag">NEW PATIENT FORM <b>pg. 1</b></div>

  <h1 class="welcome">WELCOME TO OUR PRACTICE!</h1>
  <p class="intro" lang="en"><em><i>This information is confidential</i></em> and is necessary to enable us to offer you <em><i>the best possible care.</i></em><br>At Bramwell Dental, we respect and protect the privacy of our patients and as such will only ask for information relevant to the treatment we may need to provide you. Thank you!</p>

  <div class="form">
    <div class="band">PATIENT INFORMATION</div>
    <div class="row"><span class="f">Title: <span class="box"></span>Ms. &nbsp;<span class="box"></span>Mrs. &nbsp;<span class="box"></span>Mr. &nbsp;<span class="box"></span>Master <span class="box"></span>Dr. &nbsp;<span class="box"></span>Other</span></div>
    <div class="row"><span class="f">Surname:</span><span class="f c-mid">First Name:</span></div>
    <div class="row"><span class="f">Preferred</span><span class="f c-mid">Date of Birth (dd/mth/yr):</span><span class="f slash1">/</span><span class="f slash2">/</span></div>
    <div class="row"><span class="f">Current Residential Address</span></div>
    <div class="row"></div>
    <div class="row"><span class="f c-mid">Postcode:</span></div>
    <div class="row"><span class="f">Postal Residential Address:</span></div>
    <div class="row"></div>
    <div class="row"><span class="f c-mid">Postcode:</span></div>
    <div class="row"><span class="f">Occupation</span><span class="f c-mid">Employer</span></div>
    <div class="gap-7"></div>

    <div class="band">PATIENT CONTACT INFORMATION</div>
    <div class="row tall"><span class="f">Phone: (M)</span><span class="f c-third">(H)</span><span class="f c-far">(W)</span></div>
    <div class="row tall"><span class="f">Email :</span><span class="f c-mid">Preferred:</span></div>
    <div class="row"><span class="f">Preferred method of communication:</span></div>
    <div class="row"><span class="f"><span class="box"></span>SMS</span><span class="f t2"><span class="box"></span>Phone</span><span class="f t3"><span class="box"></span>Email</span><span class="f t4"><span class="box"></span>Mail</span></div>
    <div class="gap-5"></div>

    <div class="band">EMERGENCY CONTACT</div>
    <div class="row"><span class="f">Name:</span><span class="f c-third">Relationship:</span><span class="f c-far">Contact No.:</span></div>
    <div class="gap-5"></div>

    <div class="band">OTHER INFORMATION</div>
    <div class="row"><span class="f">Person responsible for your account (if yourself, please tick this box <span class="box"></span></span></div>
    <div class="row"><span class="f">Name:</span><span class="f c-third">Relationship</span><span class="f c-far">Phone:</span></div>
    <div class="row"><span class="f">Address:</span></div>
    <div class="row"></div>
    <div class="row"><span class="f c-far">Postcode</span></div>
    <div class="row"><span class="f">Do you have Private Health Insurance?</span><span class="yn">YES/NO</span></div>
    <div class="row"><span class="f">If yes, please specify the name (e.g. CoverWell)</span></div>
    <div class="row"><span class="f">Name:</span><span class="f c-mid">Patient No.:</span></div>
    <div class="row"><span class="f">Are you claiming for your treatment under a Government Dental Benefits Scheme?</span><span class="yn">YES/NO</span></div>
    <div class="row tall"><span class="f">If yes, please tick one of the following options:</span></div>
    <div class="row"><span class="f"><span class="box"></span>CDBS</span><span class="f g2"><span class="box"></span>DVA</span><span class="f g3"><span class="box"></span>Workcover</span><span class="f g4"><span class="box"></span>MAC</span><span class="f g5"><span class="box"></span>Other</span></div>
    <div class="row note"><span>Please note: if you are claiming, please ensure that you have the relevant letters and/or forms as payment is required at the time of treatment.</span></div>
    <div class="row"><span class="f">How did you hear about us (Please tick one option below).</span></div>
    <div class="row"><span class="f"><span class="box"></span>Referred</span><span class="f g2"><span class="box"></span>Phone Directory</span><span class="f g3"><span class="box"></span>Advertisement</span><span class="f g4"><span class="box"></span>Internet</span><span class="f g5"><span class="box"></span>Other</span></div>
    <div class="row"><span class="f">If referred, please provide name of referrer:</span></div>
    <div class="row"><span class="f">Relationship to you:</span></div>
  </div>
</div>
</body>
</html>
```